Management consultant needs to update look of website

Currently I have a great word press website but it needs an updated look. I have new text for the site in the attached word document. I also have a list of websites whose design, look, and organization i like as a guide for the designer. The final design should be simple, strong, clear, and project the idea that my brand is a powerful authority in this space. Current site = www.corvelstrategy.example

Target Market(s)

company owners / executives

Industry/Entity Type

Management Consulting

Number of Pages Required

3 page

Font styles to use
Serif

Colors

Designer to choose colors to be used in the design.

Requirements
Must have
• a simple and clear design and message. professional look. easy navigation. responsive to mobile devices. an easily implemented wordpress theme OR squarespace. use of my logo colors. though I am open to changing to a deep navy or charcoal logo image. source file uploaded.
Nice to have
• i like the cover photo and logo watermark on my current homepage. i like the google map with my logo on the current contact page. i like the animation as well. a great blend of the current site and something that is more seamless.

```html
<!DOCTYPE html>
<html lang="en">
<head>
<meta charset="utf-8">
<title>Tarvane Strategy — Management Consultancy</title>
<link rel="stylesheet" href="https://fonts.googleapis.com/css2?family=Cinzel:wght@500;700&family=Poppins:wght@400;500&family=Lato:wght@400;700&display=swap">
<style>
:root{
  --gold:#cfa84a;
  --gold-deep:#b8923a;
  --ink:#1b1b1b;
  --text:#555;
  --muted:#9a9a9a;
  --paper:#ffffff;
  --mist:#f4f4f4;
  --line:#e6e6e6;
}
*{margin:0;padding:0;box-sizing:border-box}
html,body{width:1200px;height:3066px;overflow:hidden;background:var(--paper)}
body{position:relative;font-family:'Lato',sans-serif;color:var(--text)}
.abs{position:absolute}
.topline{left:0;top:0;width:1200px;height:9px;background:var(--gold)}

/* header */
.site-header{left:0;top:9px;width:1200px;height:118px;background:var(--paper)}
.brand{left:82px;top:18px;display:flex;align-items:center;gap:14px}
.brand-dot{width:68px;height:68px;border-radius:50%;background:var(--gold)}
.brand-rule{width:2px;height:70px;background:var(--gold)}
.brand-name{font-family:'Cinzel',serif;font-weight:700;color:var(--gold);font-size:25px;line-height:26px}
.brand-tag{font-family:'Lato',sans-serif;color:var(--gold);font-size:11px;margin-top:4px}
.nav{left:497px;top:54px;font-family:'Poppins',sans-serif;font-size:16px;color:#555}
.nav a{position:absolute;white-space:nowrap;text-decoration:none;color:#555}
.nav a.active{color:var(--ink);font-weight:500}
.search{left:1070px;top:45px;width:54px;height:54px;border-radius:50%;background:#efefef;border:1px solid #e2e2e2;display:flex;align-items:center;justify-content:center}

/* hero */
.hero{left:0;top:127px;width:1200px;height:572px;background:linear-gradient(180deg,#d9dcdf 0%,#b9bdc2 45%,#eceef0 100%)}
.hero-mark{left:508px;top:225px;width:184px;height:184px;border-radius:50%;background:#2a2a2a;display:flex;align-items:center;justify-content:center}
.hero-mark span{width:130px;height:130px;border-radius:50%;background:var(--gold)}
.hero-title{left:327px;top:440px;width:548px;height:87px;background:rgba(40,40,40,.82);display:flex;align-items:center;justify-content:center;font-family:'Cinzel',serif;font-weight:700;color:var(--gold);font-size:44px;letter-spacing:1px;white-space:nowrap}
.hero-sub{left:0;top:538px;width:1200px;text-align:center;font-family:'Cinzel',serif;font-weight:700;color:#111;font-size:44px}

/* section titles */
.title{width:1200px;left:0;text-align:center;font-family:'Poppins',sans-serif;font-weight:500;color:var(--ink);font-size:36px;line-height:47px}
.copy{text-align:center;font-size:16.5px;line-height:31px;color:#8a8a8a}

/* feedback */
.feedback{left:0;top:1114px;width:1200px;height:409px;background:linear-gradient(90deg,#f0f0f0,#f7f7f7)}
.feedback-photo{left:593px;top:1114px;width:607px;height:409px;background:linear-gradient(120deg,#e9e9e9 0%,#cfcfcf 45%,#6b5a52 75%,#3a3230 100%);clip-path:polygon(18% 0,100% 0,100% 100%,0 100%)}
.feedback h2{position:absolute;left:80px;top:96px;font-family:'Poppins',sans-serif;font-weight:500;font-size:36px;color:var(--ink)}
.feedback p{position:absolute;left:80px;top:164px;width:535px;font-size:16px;line-height:31px;color:#333}

/* testimonials */
.quote-mark{left:540px;top:1638px;font-family:'Cinzel',serif;font-size:170px;line-height:1;color:var(--gold);opacity:.18}
.avatar{border-radius:50%;border:3px solid #fff;box-shadow:0 0 0 1px #ddd}
.person{left:0;top:1870px;width:1200px;text-align:center;font-family:'Lato',sans-serif;font-weight:700;font-size:15px;color:var(--gold);letter-spacing:1px}

/* partners */
.partners{left:0;top:1983px;width:1200px;height:501px;background:var(--mist)}
.partner{width:192px;height:74px;background:#fff;border:1px solid var(--line);display:flex;align-items:center;justify-content:center}
.partner span{width:110px;height:30px;border-radius:4px;background:#cfcfcf}
.partner.featured span{background:#58c4b5}

/* cta */
.field{top:2755px;height:58px;background:#f1f1f1;border-radius:6px;display:flex;align-items:center;gap:12px;padding-left:18px;font-size:15px;color:#333}
.button{left:713px;top:2752px;width:313px;height:62px;border-radius:31px;background:var(--gold);color:#fff;font-size:19px;display:flex;align-items:center;justify-content:center}
.fine{left:0;top:2854px;width:1200px;text-align:center;font-size:13.5px;line-height:23px;color:#555}

/* footer */
.site-footer{left:0;top:2964px;width:1200px;height:102px;background:var(--gold)}
.site-footer p{position:absolute;left:80px;top:40px;font-size:13px;color:#fff}
.social{top:2988px;width:52px;height:52px;border-radius:50%;background:#fff;display:flex;align-items:center;justify-content:center;font-size:11px;font-weight:700;color:var(--ink)}
</style>
</head>
<body>
<div class="abs topline"></div>

<header class="abs site-header">
  <div class="abs brand">
    <div class="brand-dot"></div>
    <div class="brand-rule"></div>
    <div>
      <div class="brand-name">TARVANE<br>STRATEGY</div>
      <div class="brand-tag">Strategy. Workshops. Coaching.</div>
    </div>
  </div>
  <nav class="abs nav">
    <a class="active" style="left:0">HOME</a>
    <a style="left:90px">ABOUT</a>
    <a style="left:194px">SERVICES</a>
    <a style="left:318px">ARTICLES</a>
    <a style="left:440px">CONTACT</a>
  </nav>
  <div class="abs search">
    <svg width="22" height="22" viewBox="0 0 22 22" fill="none" stroke="#999" stroke-width="2"><circle cx="9" cy="9" r="6.5"/><line x1="14" y1="14" x2="20" y2="20"/></svg>
  </div>
</header>

<section>
  <div class="abs hero" role="img" aria-label="Business team in a meeting around a conference table"></div>
  <div class="abs hero-mark"><span></span></div>
  <div class="abs hero-title">TARVANE STRATEGY</div>
  <div class="abs hero-sub">MANAGEMENT CONSULTANCY</div>
</section>

<section>
  <h1 class="abs title" style="top:757px">Great Companies Succeed by<br>Investing in the Right People</h1>
  <p class="abs copy" style="left:222px;top:880px;width:756px">It’s no secret that long-term business success requires a smart investment in the right people for your company. And yet, knowing how to cultivate a strong staff and keep them focused on the road ahead can be challenging for even the savviest organizational leaders and human resource executives.</p>
  <p class="abs copy" style="left:222px;top:995px;width:756px">I’m Dr. Mara Ellison and I want to help business owners, leaders, and HR teams understand how to identify, develop, and retain talented professionals who can take your success to the next level.</p>
</section>

<section class="abs feedback">
  <h2>Clients Feedback</h2>
  <p>Lorem ipsum dolor sit amet, consectetur adipiscing elit, sed do eiusmod tempor incididunt ut labore et dolore magna aliqua. Ut enim ad minim veniam, quis nostrud exercitation ullamco laboris nisi ut aliquip ex ea commodo consequat.</p>
</section>
<div class="abs feedback-photo" role="img" aria-label="Thoughtful businesswoman in glasses by an office window"></div>

<section>
  <h2 class="abs title" style="top:1588px">What Our Clients Say</h2>
  <div class="abs quote-mark">“</div>
  <p class="abs copy" style="left:250px;top:1653px;width:700px;color:#aaa;font-size:15px;line-height:26px">Lorem ipsum dolor sit amet, consectetur adipiscing elit, sed do eiusmod tempor incididunt ut labore et dolore magna aliqua. Ut enim ad minim veniam, quis nostrud exercitation ullamco laboris nisi ut aliquip ex ea commodo consequat.</p>
  <svg class="abs" style="left:256px;top:1795px" width="50" height="20" viewBox="0 0 50 20" fill="none" stroke="#cfa84a" stroke-width="2.5"><line x1="3" y1="10" x2="48" y2="10"/><polyline points="12,2 3,10 12,18"/></svg>
  <svg class="abs" style="left:894px;top:1795px" width="50" height="20" viewBox="0 0 50 20" fill="none" stroke="#777" stroke-width="2.5"><line x1="2" y1="10" x2="47" y2="10"/><polyline points="38,2 47,10 38,18"/></svg>
  <div class="abs avatar" style="left:460px;top:1768px;width:74px;height:74px;background:linear-gradient(160deg,#dfe6ee,#b7c3cf)" role="img" aria-label="Client portrait"></div>
  <div class="abs avatar" style="left:554px;top:1758px;width:94px;height:94px;background:linear-gradient(160deg,#e8edf2,#9fb0c2)" role="img" aria-label="Client portrait"></div>
  <div class="abs avatar" style="left:666px;top:1768px;width:74px;height:74px;background:linear-gradient(160deg,#e6e1dc,#b9aca2)" role="img" aria-label="Client portrait"></div>
  <div class="abs person">DEVIN R. OAKES</div>
</section>

<section class="abs partners">
  <h2 class="abs title" style="top:56px">Selected Partners Clients</h2>
</section>
<div class="abs partner" style="left:78px;top:2128px"><span></span></div>
<div class="abs partner" style="left:291px;top:2128px"><span></span></div>
<div class="abs partner featured" style="left:503px;top:2128px"><span></span></div>
<div class="abs partner" style="left:716px;top:2128px"><span></span></div>
<div class="abs partner" style="left:929px;top:2128px"><span></span></div>
<div class="abs partner" style="left:78px;top:2232px"><span></span></div>
<div class="abs partner" style="left:291px;top:2232px"><span></span></div>
<div class="abs partner" style="left:503px;top:2232px"><span></span></div>
<div class="abs partner" style="left:716px;top:2232px"><span></span></div>
<div class="abs partner" style="left:929px;top:2232px"><span></span></div>
<div class="abs partner" style="left:78px;top:2336px"><span></span></div>
<div class="abs partner" style="left:291px;top:2336px"><span></span></div>
<div class="abs partner" style="left:503px;top:2336px"><span></span></div>
<div class="abs partner" style="left:716px;top:2336px"><span></span></div>
<div class="abs partner" style="left:929px;top:2336px"><span></span></div>

<section>
  <h2 class="abs title" style="top:2540px">Learn to Inspire Employees and Unlock<br>Their Maximum Potential</h2>
  <p class="abs copy" style="left:272px;top:2654px;width:656px">If you’re struggling to connect with today’s employees and you need to develop a better way to lead them, I want to help you become the very best leader possible.</p>
  <div class="abs field" style="left:174px;width:259px">
    <svg width="20" height="20" viewBox="0 0 20 20" fill="#222"><circle cx="10" cy="6" r="4.5"/><path d="M1 20c0-5 4-8 9-8s9 3 9 8z"/></svg>First Name :
  </div>
  <div class="abs field" style="left:444px;width:259px">
    <svg width="22" height="16" viewBox="0 0 22 16" fill="#222"><path d="M0 0h22v2L11 9 0 2z"/><path d="M0 4l11 7 11-7v12H0z"/></svg>Email :
  </div>
  <div class="abs button">Download Free Information</div>
  <p class="abs fine">* You’ll receive monthly updates filled with leader-focused resources and helpful information that will<br>help you build stronger organizational leaders. You can unsubscribe at any time.</p>
</section>

<footer class="abs site-footer">
  <p>Copyright © <b>TARVANE STRATEGY</b> - 2019 . All right Reserved</p>
</footer>
<div class="abs social" style="left:945px">Pro</div>
<div class="abs social" style="left:1008px">Fan</div>
<div class="abs social" style="left:1071px">Pic</div>
</body>
</html>
```